Stanbrook Fire Services Pty Ltd

We need business cards for a company based in Perth, we install, service and maintain fire equipment.
On the front we want a great design with our logo and a small spot for our full company name, general company email address and office number. On the back we need space for our name, title, mobile number and email address on the back.

Target Market(s)

Facility managers and commercial/industrial building owners/occupiers.

Contact Information for Business Card

Font styles to use
Sans Serif

Requirements
Must have
• Please only submit 5 of your best samples.
Darker tones are preferred.
Nice to have
• We want to use, black, red and grey. Keep it modern and clean.
I've attached the company logo and a sample of a boarder we use on our emergency plans.
Should not have
• No preference. Let the designer choose.

```html
<!DOCTYPE html>
<html lang="en">
<head>
<meta charset="utf-8">
<title>Stanbrook Fire Services – Business Cards</title>
<link rel="stylesheet" href="https://fonts.googleapis.com/css2?family=Hind:wght@300;400;600;700&display=swap">
<style>
  :root {
    --canvas: #e8ebe6;
    --black: #000000;
    --white: #ffffff;
    --red: #ec2530;
    --ink: #1a1a1a;
  }
  * { margin: 0; padding: 0; box-sizing: border-box; }
  html, body {
    width: 1200px; height: 1200px; overflow: hidden;
    background: var(--canvas);
    font-family: "Hind", Arial, sans-serif;
  }
  .canvas { position: relative; width: 1200px; height: 1200px; }

  .card { position: absolute; width: 709px; height: 405px; overflow: hidden; }

  /* Wordmark: plain name with a plain square */
  .wordmark {
    position: absolute; display: flex; align-items: center; gap: 12px;
    color: var(--red); font-weight: 600; line-height: 1; white-space: nowrap;
  }
  .wordmark-square { display: block; background: var(--red); flex: none; }

  /* Front */
  .card--front { left: 246px; top: 148px; background: var(--black); color: var(--white); }
  .card--front .wordmark { right: 40px; top: 72px; font-size: 46px; }
  .card--front .wordmark-square { width: 30px; height: 30px; }
  .company-name {
    position: absolute; left: 45px; top: 208px;
    font-weight: 600; font-size: 31px; line-height: 1.2; white-space: nowrap;
  }
  .company-contact {
    position: absolute; left: 45px; top: 258px;
    font-weight: 400; font-size: 24px; line-height: 25.5px;
  }

  /* Back */
  .card--back { left: 248px; top: 653px; background: var(--white); color: var(--ink); }
  .card--back .wordmark { right: 22px; top: 48px; font-size: 38px; }
  .card--back .wordmark-square { width: 24px; height: 24px; }
  .name-banner { position: absolute; left: 0; top: 55px; width: 312px; height: 74px; }
  .person { position: absolute; left: 52px; top: 62px; color: var(--white); }
  .person-name { font-size: 34px; line-height: 36px; color: var(--red); font-weight: 300; white-space: nowrap; }
  .person-name strong { font-weight: 700; }
  .person-title { font-size: 23px; line-height: 26px; font-weight: 400; }
  .contact-rule { position: absolute; left: 0; top: 323px; width: 709px; height: 2px; background: var(--red); }
  .contact-item { position: absolute; top: 312px; }
  .contact-label {
    display: inline-block; background: var(--white); padding: 0 2px;
    font-size: 18px; line-height: 22px; font-weight: 400;
  }
  .contact-value { font-size: 20px; line-height: 24px; margin-top: 2px; padding-left: 2px; white-space: nowrap; }
  .contact-item--phone { left: 28px; }
  .contact-item--email { left: 223px; }
  .contact-item--address { left: 455px; }
</style>
</head>
<body>
<main class="canvas">
  <section class="card card--front" aria-label="Business card front">
    <div class="wordmark"><span class="wordmark-square" aria-hidden="true"></span>Stanbrook</div>
    <h1 class="company-name">Stanbrook Fire Services Pty Ltd</h1>
    <p class="company-contact">
      123 Street Name, State,<br>
      Country Pincode.<br>
      Ph: +000 12345678<br>
      email@hostname.com
    </p>
  </section>

  <section class="card card--back" aria-label="Business card back">
    <svg class="name-banner" viewBox="0 0 312 74" aria-hidden="true">
      <polygon points="0,0 312,0 284,37 312,74 0,74" fill="var(--black)"/>
    </svg>
    <div class="person">
      <h2 class="person-name">FIRST <strong>NAME</strong></h2>
      <p class="person-title">Designation</p>
    </div>
    <div class="wordmark"><span class="wordmark-square" aria-hidden="true"></span>Stanbrook</div>
    <div class="contact-rule"></div>
    <div class="contact-item contact-item--phone">
      <span class="contact-label">Phone</span>
      <p class="contact-value">1234-5678-9123</p>
    </div>
    <div class="contact-item contact-item--email">
      <span class="contact-label">Email</span>
      <p class="contact-value">email@hostname.com</p>
    </div>
    <div class="contact-item contact-item--address">
      <span class="contact-label">Address</span>
      <p class="contact-value">123 Street Name, Pincode.</p>
    </div>
  </section>
</main>
</body>
</html>
```